Real Estate Brochure/ door flyer.

I am looking for a brochure that can be put in a plastic door hanger bag and distributed as I walk throughout neighborhoods. It should be mainly directed towards Sellers, but have a nod to Buyers as well since once sold, the person will need to buy.
I was planning on a tri fold brochure, but am open to other styles. I do have a bio, and am on the fence as to whether or not to include it.

Target Market(s)

Owners of residential homes and potential buyers of the same

Industry/Entity Type

Real Estate

Colors

Designer to choose colors to be used in the design.

Requirements
Must have
• The service promises I have made, our logo,
• My contact information, email and cell phone.
• I'm looking for something bright and clean looking.
• There is an equal housing opportunity symbol and Dwellmark symbol that is required by law, I am trying to find artwork for it. As well as "Not intended to solicit represented parties" has to be on the brochure somewhere.
Nice to have
• Photos of homeowner's in a nice home. I like mixed family relationships. Interracial, same sex couples and young couples just starting out.
Should not have
• Any form of deadline or timeline to respond.

```html
<!DOCTYPE html>
<html lang="en">
<head>
<meta charset="utf-8">
<title>Halvorsen Real Estate – Tri-fold Brochure</title>
<link rel="stylesheet" href="https://fonts.googleapis.com/css2?family=Montserrat:wght@500;600;700&family=Lato:wght@400;700&family=Arimo:wght@400;700&display=swap">
<style>
  :root{
    --red:#9b1c24;
    --red-dark:#7d141b;
    --ink:#1f1f1f;
    --body:#333;
    --grey:#d8d8d8;
    --grey-dark:#b9b9b9;
    --page:#ffffff;
    --backdrop:#e2e2e2;
  }
  *{box-sizing:border-box;margin:0;padding:0}
  html,body{width:1200px;height:1200px;overflow:hidden;background:var(--backdrop)}
  body{font-family:"Lato",sans-serif;color:var(--body);position:relative}

  .brochure{position:absolute;left:30px;top:160px;width:1140px;height:880px;display:flex;background:var(--page);box-shadow:0 6px 24px rgba(0,0,0,.15)}
  .panel{position:relative;width:380px;height:880px;overflow:hidden;background:linear-gradient(180deg,#fff 0%,#f4f4f4 100%)}
  .panel + .panel{border-left:1px solid #ececec}

  /* ---------- inside-left panel ---------- */
  .intro{position:absolute;left:26px;top:34px;right:26px;font-size:13px;line-height:1.35;color:var(--ink)}
  .promise-band{position:absolute;left:0;top:112px;width:360px;height:50px;background:var(--red);color:#fff;font-size:14px;line-height:1.25;padding:7px 24px;clip-path:polygon(0 0,100% 0,94% 100%,0 100%)}
  .promise-list{position:absolute;left:24px;right:22px;top:180px;list-style:none}
  .promise-list li{position:relative;padding-left:22px;font-size:12.5px;line-height:1.32;text-align:justify;margin-bottom:14px;color:var(--ink)}
  .promise-list li svg{position:absolute;left:0;top:3px}
  .home-photo{position:absolute;left:0;top:560px;width:380px;height:320px;background:linear-gradient(180deg,#cfd9c4 0%,#b39a84 35%,#8e6f5b 55%,#5f8a3c 75%,#4a7a2c 100%)}
  .cta-ribbon{position:absolute;left:0;bottom:40px;background:var(--red);color:#fff;font-size:13.5px;padding:5px 26px 5px 26px;clip-path:polygon(0 0,100% 0,95% 100%,0 100%)}
  .cta-phone{position:absolute;left:0;bottom:10px;background:var(--red);color:#fff;font-size:13.5px;padding:4px 22px 4px 26px;display:flex;align-items:center;gap:6px;clip-path:polygon(0 0,100% 0,93% 100%,0 100%)}

  /* ---------- inside-middle panel ---------- */
  .handover-photo{position:absolute;left:0;top:0;width:380px;height:300px;background:linear-gradient(180deg,#6fa6e0 0%,#c9c7c0 38%,#b8a79a 55%,#6da04a 80%,#4f8a2f 100%);clip-path:polygon(0 0,100% 0,100% 64%,88% 60%,0 100%)}
  .section-title{font-family:"Montserrat",sans-serif;font-weight:600;font-size:14px;color:var(--red);letter-spacing:.01em;text-transform:uppercase}
  .benefits{position:absolute;left:30px;right:20px;top:318px}
  .reasons{position:absolute;left:30px;right:20px;top:430px}
  .check-list{list-style:none;margin-top:8px}
  .check-list li{position:relative;padding-left:22px;font-size:12.5px;line-height:1.25;margin-bottom:5px;color:var(--ink)}
  .check-list li svg{position:absolute;left:0;top:1px}
  .mid-band{position:absolute;left:0;top:560px;width:380px;height:110px}
  .brand{font-family:"Montserrat",sans-serif;font-weight:600;color:var(--red);display:flex;align-items:center;gap:8px;letter-spacing:.1em;text-transform:uppercase;white-space:nowrap}
  .brand .mark{width:11px;height:11px;background:var(--red);flex:none}
  .brand-mid{position:absolute;right:26px;top:676px;font-size:14px}
  .contact{position:absolute;left:34px;right:20px;top:712px}
  .contact-list{list-style:none;margin-top:10px}
  .contact-list li{display:flex;align-items:flex-start;gap:12px;font-size:12.5px;line-height:1.25;color:var(--ink);margin-bottom:9px}
  .contact-list svg{flex:none;margin-top:1px}

  /* ---------- cover panel ---------- */
  .brand-cover{position:absolute;left:0;right:0;top:54px;justify-content:center;font-size:18px}
  .family-photo{position:absolute;left:0;top:130px;width:380px;height:440px;background:linear-gradient(180deg,#f2f2f0 0%,#b7a99a 28%,#9c8a7b 48%,#6e9e45 72%,#4f8a2e 100%);clip-path:polygon(0 0,100% 0,100% 82%,82% 100%,0 88%)}
  .cover-red{position:absolute;left:0;top:500px;width:380px;height:90px}
  .headline{position:absolute;left:0;right:22px;top:612px;text-align:right;font-family:"Arimo",sans-serif;line-height:1.12}
  .headline .l1{display:block;font-weight:700;font-size:31px;color:#111}
  .headline .l2{display:block;font-size:29px;color:var(--red)}
  .headline .l3{display:block;font-size:24px;color:#111}
  .web-line{position:absolute;left:20px;right:22px;top:756px;display:flex;align-items:center;gap:8px;font-size:11.5px;color:var(--ink)}
  .web-line .rule{flex:1;height:1.5px;background:var(--red)}
  .cover-corner{position:absolute;right:0;bottom:0;width:380px;height:120px}
</style>
</head>
<body>
<svg width="0" height="0" style="position:absolute">
  <defs>
    <symbol id="tick" viewBox="0 0 16 16"><circle cx="8" cy="8" r="6.6" fill="none" stroke="#9b1c24" stroke-width="1.8"/><path d="M4.8 8.2l2.2 2.2 4.3-4.6" fill="none" stroke="#9b1c24" stroke-width="1.9" stroke-linecap="round" stroke-linejoin="round"/></symbol>
  </defs>
</svg>

<main class="brochure">
  <!-- inside left -->
  <section class="panel panel-promise">
    <p class="intro">Are you ready to purchase, sell, or rent a house? Get in touch with us today! We have an experience of more than 10 years in the real estate business and can help you find the home of your dreams.</p>
    <h2 class="promise-band">My promise of services to you as a professional Real Estate Agent</h2>
    <ul class="promise-list">
      <li><svg width="14" height="14"><use href="#tick"/></svg>Professional courteous communication. With weekly updates and feedback from Agents and the potential Buyers that have been through your home.</li>
      <li><svg width="14" height="14"><use href="#tick"/></svg>No Lockboxes! I do not subscribe to an Agent putting a lockbox on your home and disappearing, only to miraculously show up at the closing. I will meet all potential Buyers and walk them through your home, pointing out it's highlights and enlisting their feedback on your home.</li>
      <li><svg width="14" height="14"><use href="#tick"/></svg>I will provide professional advice on how to stage and prepare your home for a showing from the prospective of the Buyer.</li>
      <li><svg width="14" height="14"><use href="#tick"/></svg>Open Houses. I make every attempt to perform two open houses every month. Yours could be next!</li>
      <li><svg width="14" height="14"><use href="#tick"/></svg>Referral system. Not ready to sell? Maybe you know someone that is considering selling or someone looking to buy a home. Send me their contact information and if it leads to a sale or a purchase, I will give you a gift certificate good for dinner for two at a local restaurant!</li>
    </ul>
    <div class="home-photo" role="img" aria-label="Photo of a young family sitting on the lawn in front of a brick house"></div>
    <p class="cta-ribbon">Call us today to schedule an appointment</p>
    <p class="cta-phone"><svg width="11" height="11" viewBox="0 0 24 24"><path fill="#fff" d="M6.6 10.8a15.1 15.1 0 006.6 6.6l2.2-2.2c.3-.3.7-.4 1-.2 1.1.4 2.3.6 3.6.6.6 0 1 .4 1 1V20c0 .6-.4 1-1 1A17 17 0 013 4c0-.6.4-1 1-1h3.5c.6 0 1 .4 1 1 0 1.3.2 2.5.6 3.6.1.3 0 .7-.2 1z"/></svg>555-017-3846</p>
  </section>

  <!-- inside middle -->
  <section class="panel panel-benefits">
    <div class="handover-photo" role="img" aria-label="Photo of house keys being handed over in front of a house with a sold sign"></div>
    <div class="benefits">
      <h3 class="section-title">Benefits of real estate</h3>
      <ul class="check-list">
        <li><svg width="14" height="14"><use href="#tick"/></svg>Find the right property at the right cost</li>
        <li><svg width="14" height="14"><use href="#tick"/></svg>Generate immediate profit by renting out the place</li>
        <li><svg width="14" height="14"><use href="#tick"/></svg>Secure investment to take care of your family after your demise</li>
      </ul>
    </div>
    <div class="reasons">
      <h3 class="section-title">Reasons for choosing us</h3>
      <ul class="check-list">
        <li><svg width="14" height="14"><use href="#tick"/></svg>More than 10 years of experience</li>
        <li><svg width="14" height="14"><use href="#tick"/></svg>Locally owned and operated</li>
        <li><svg width="14" height="14"><use href="#tick"/></svg>FREE comparative market analysis</li>
        <li><svg width="14" height="14"><use href="#tick"/></svg>Friendly and customer oriented</li>
        <li><svg width="14" height="14"><use href="#tick"/></svg>Quick turnaround times</li>
      </ul>
    </div>
    <svg class="mid-band" viewBox="0 0 380 110" preserveAspectRatio="none" aria-hidden="true">
      <polygon points="0,70 120,72 380,0 380,14 125,86 0,84" fill="#c9c9c9"/>
      <polygon points="0,84 125,86 110,98 0,92" fill="#9b1c24"/>
    </svg>
    <p class="brand brand-mid"><span class="mark"></span>Halvorsen Real Estate</p>
    <div class="contact">
      <h3 class="section-title">Contact us</h3>
      <ul class="contact-list">
        <li><svg width="16" height="18" viewBox="0 0 24 24"><path fill="#9b1c24" d="M12 2a7 7 0 00-7 7c0 5 7 13 7 13s7-8 7-13a7 7 0 00-7-7zm0 9.5A2.5 2.5 0 1112 6a2.5 2.5 0 010 5.5z"/></svg><span>88 Maple Row<br>88 Maple Row, Ashford Falls, CT 06100, USA</span></li>
        <li><svg width="16" height="16" viewBox="0 0 24 24"><path fill="none" stroke="#9b1c24" stroke-width="2" d="M6.6 10.8a15.1 15.1 0 006.6 6.6l2.2-2.2c.3-.3.7-.4 1-.2 1.1.4 2.3.6 3.6.6.6 0 1 .4 1 1V20c0 .6-.4 1-1 1A17 17 0 013 4c0-.6.4-1 1-1h3.5c.6 0 1 .4 1 1 0 1.3.2 2.5.6 3.6.1.3 0 .7-.2 1z"/></svg><span>555-014-2290</span></li>
        <li><svg width="16" height="14" viewBox="0 0 24 20"><rect x="1" y="2" width="22" height="16" rx="2" fill="#9b1c24"/><path d="M2 4l10 7 10-7" fill="none" stroke="#fff" stroke-width="1.8"/></svg><span>info@halvorsenhomes.com</span></li>
        <li><svg width="16" height="16" viewBox="0 0 24 24"><g fill="none" stroke="#9b1c24" stroke-width="1.8"><circle cx="12" cy="12" r="10"/><ellipse cx="12" cy="12" rx="4.5" ry="10"/><path d="M2 12h20M4 6.5h16M4 17.5h16"/></g></svg><span>www.halvorsenhomes.com</span></li>
      </ul>
    </div>
  </section>

  <!-- cover -->
  <section class="panel panel-cover">
    <p class="brand brand-cover"><span class="mark"></span>Halvorsen Real Estate</p>
    <svg class="cover-red" viewBox="0 0 380 90" preserveAspectRatio="none" aria-hidden="true">
      <polygon points="0,16 312,70 380,20 380,34 312,84 0,30" fill="#9b1c24"/>
    </svg>
    <div class="family-photo" role="img" aria-label="Photo of a smiling family of five standing on the lawn in front of their stone house"></div>
    <h1 class="headline">
      <span class="l1">Helping You Find</span>
      <span class="l2">the Right Residential</span>
      <span class="l3">and Commercial Property</span>
    </h1>
    <p class="web-line"><span class="rule"></span><span>www.halvorsenhomes.com</span><span class="rule"></span></p>
    <svg class="cover-corner" viewBox="0 0 380 120" preserveAspectRatio="none" aria-hidden="true">
      <polygon points="230,120 380,40 380,120" fill="#e2e2e2"/>
      <polygon points="260,120 380,60 380,120" fill="#9b1c24"/>
    </svg>
  </section>
</main>
</body>
</html>
```